Tevrix BIM business website

I have a logo design and business card concept is ongoing at this point, but i need a website design based on VDC or BIM ("Virtual Building and Construction" or "Building Information Modeling") that will stand out for the quality and concept that we provide. I am a consultant providing training and production work for Quorvel (Zembrick application <where most of the overview can be obtained>). We are providing BIM production and coordination services as well. I can fill in the meat but I need an open development website. Currently, just obtaining a domain so it can be included on a business card is the quickest objective, then developing the content and launching it.

Business

```html
<!DOCTYPE html>
<html lang="en">
<head>
<meta charset="utf-8">
<title>Tevrix BIM Consulting</title>
<link rel="stylesheet" href="https://fonts.googleapis.com/css2?family=Montserrat:wght@300;400;600;700;800&display=swap">
<style>
:root{
  --ink:#111111;
  --navy:#1d2b5c;
  --hero-top:#15396b;
  --hero-bottom:#2a6aa3;
  --arrow:#8c8c8c;
  --section:#e8ebee;
  --white:#ffffff;
  --accent:#d9731c;
  --muted:#9a9a9a;
  --body:#2a2a2a;
}
*{margin:0;padding:0;box-sizing:border-box}
html,body{width:800px;height:1200px;overflow:hidden;background:var(--white)}
body{position:relative;font-family:'Montserrat',sans-serif;color:var(--ink)}
.abs{position:absolute}

.brand{left:370px;top:18px;width:62px;height:51px;background:var(--navy);display:flex;align-items:center;justify-content:center;color:var(--white);font-weight:600;font-size:12px;letter-spacing:.5px}
.menu{left:687px;top:31px;display:flex;align-items:center;gap:6px;font-size:6px;letter-spacing:1.2px;color:var(--muted)}
.menu svg{display:block}

.hero{left:86px;top:82px;width:624px;height:350px;background:linear-gradient(180deg,var(--hero-top),var(--hero-bottom))}
.hero-kicker{left:132px;top:146px;color:var(--white);font-weight:300;font-size:24px}
.hero-title{left:131px;top:170px;color:var(--white);font-weight:700;font-size:40px;letter-spacing:.3px;white-space:nowrap}
.arrow-btn{width:24px;height:24px;background:var(--arrow);top:210px;display:flex;align-items:center;justify-content:center}
.arrow-prev{left:57px}
.arrow-next{left:716px}
.scroll-cue{left:371px;top:442px;font-size:8px;color:var(--body);display:flex;align-items:center;gap:5px}

.about{left:3px;top:502px;width:791px;height:312px;background:var(--section)}
.about-card{left:94px;top:547px;width:288px;height:218px;background:var(--white)}
.about-photo{left:382px;top:546px;width:328px;height:219px;background:linear-gradient(135deg,#c9c4bb 0%,#eae8e4 45%,#d8d8d6 70%,#3a4a78 100%)}
.section-title{font-weight:700;font-size:12.5px;letter-spacing:.2px}
.rule{height:2px;width:16px;background:var(--ink)}
.about-title{left:118px;top:549px}
.about-rule{left:118px;top:566px}
.about-copy{left:118px;top:591px;width:256px;font-size:6.3px;line-height:12.4px;color:var(--body)}
.about-copy p+p{margin-top:12.4px}
.learn-more{left:119px;top:710px;font-size:5.2px;font-weight:700;letter-spacing:1.3px;color:var(--accent)}
.tick-bar{left:94px;top:740px;width:2px;height:10px;background:var(--ink)}
.side-label{font-size:6px;font-weight:700;letter-spacing:.4px;transform:rotate(-90deg);transform-origin:left top;white-space:nowrap}
.about-label{left:72px;top:747px}

.services-title{left:94px;top:862px}
.services-rule{left:94px;top:888px}
.service-caption{font-size:5.4px;font-weight:600;letter-spacing:1.3px;white-space:nowrap}
.cap-training{left:203px;top:944px}
.cap-production{left:456px;top:941px}
.tile-dark{left:279px;top:1128px;width:164px;height:72px;background:#444546}
.tile-dark::after{content:"";position:absolute;left:4px;top:6px;right:8px;bottom:0;border:1px solid #8a8a8a;border-bottom:none}
.photo-training{left:76px;top:954px;width:299px;height:200px;background:linear-gradient(135deg,#eef0f1 0%,#5d7f93 40%,#2e4c5e 70%,#e9ebec 100%)}
.photo-facade{left:469px;top:948px;width:136px;height:204px;background:linear-gradient(160deg,#cfc9c0,#8b8478 60%,#5e5850)}
.facade-link{left:514px;top:1124px;font-size:6px;font-weight:700;letter-spacing:1.6px;color:var(--white)}
.photo-chart{left:567px;top:1128px;width:165px;height:72px;background:linear-gradient(90deg,#eceff2,#dfe3e6)}
.offer-label{left:72px;top:1173px}
</style>
</head>
<body>

<header>
  <div class="abs brand">Tevrix</div>
  <div class="abs menu">MENU
    <svg width="17" height="11" viewBox="0 0 17 11"><g stroke="#111" stroke-width="1.4"><line x1="0" y1="1" x2="17" y2="1"/><line x1="0" y1="5.5" x2="17" y2="5.5"/><line x1="0" y1="10" x2="17" y2="10"/></g></svg>
  </div>
</header>

<section>
  <div class="abs hero" role="img" aria-label="Blue building information model wireframe with rising data columns"></div>
  <div class="abs hero-kicker">Building</div>
  <h1 class="abs hero-title">INFORMATION MODELING</h1>
  <div class="abs arrow-btn arrow-prev"><svg width="10" height="8" viewBox="0 0 10 8"><path d="M9.5 4H1M4 1 1 4l3 3" fill="none" stroke="#fff" stroke-width="1"/></svg></div>
  <div class="abs arrow-btn arrow-next"><svg width="10" height="8" viewBox="0 0 10 8"><path d="M.5 4H9M6 1l3 3-3 3" fill="none" stroke="#fff" stroke-width="1"/></svg></div>
  <div class="abs scroll-cue">Scroll For More
    <svg width="6" height="11" viewBox="0 0 6 11"><path d="M3 0v10M.5 7.5 3 10l2.5-2.5" fill="none" stroke="#888" stroke-width=".8"/></svg>
  </div>
</section>

<section>
  <div class="abs about"></div>
  <div class="abs about-card"></div>
  <div class="abs about-photo" role="img" aria-label="Marble pencil cup with pens beside a laptop on a white desk"></div>
  <h2 class="abs section-title about-title">THE CREATIVE SIDE OF US</h2>
  <div class="abs rule about-rule"></div>
  <div class="abs about-copy">
    <p>Sed libero enim, rhoncus vel malesuada ac, euismod a velit. Morbi pellentesque eleifend lectus quis congue. Aenean quis tellus tortor, quis fermentum diam. Pellentesque molestie, dolor et tempor molestie, dui ipsum egestas elit.</p>
    <p>Nulla et dolor enim. Cras tempus semper neque. Cras tincidunt ante eget turpis dapibus eleifend. Ut sodales sagittis orci, et tristique ipsum iaculis sed. Fusce nec tortor id justo ultrices luctus et vel justo.</p>
  </div>
  <div class="abs learn-more">LEARN MORE</div>
  <div class="abs tick-bar"></div>
  <div class="abs side-label about-label">ABOUT US</div>
</section>

<section>
  <h2 class="abs section-title services-title">OUR SERVICES</h2>
  <div class="abs rule services-rule"></div>
  <div class="abs service-caption cap-training">CONSULTANT PROVIDING TRAINING</div>
  <div class="abs service-caption cap-production">PRODUCTION WORK FOR QUORVEL</div>
  <div class="abs tile-dark" role="img" aria-label="Dark service tile with plant detail"></div>
  <div class="abs photo-training" role="img" aria-label="Hand sketching on a tablet with a stylus"></div>
  <div class="abs photo-facade" role="img" aria-label="Modern building facade with rounded windows"></div>
  <div class="abs facade-link">+ LEARN MORE</div>
  <div class="abs photo-chart" role="img" aria-label="Analytics report with a pie chart on screen"></div>
  <div class="abs side-label offer-label">WHAT WE OFFER</div>
</section>

</body>
</html>
```